Need Primer (paint) Label Design

THE ATTACHED LABEL/S ARE SOLEY FOR REFERENCE. DO NOT MAKE ME AN INTERIOR PAINT OR CHALK PAINT LABEL. I ONLY NEED A "PRIMER" LABEL. THE ATTACHED INTERIOR PAINT LABEL IS ONLY TO SHOW YOU THE THEME/DESIGN OF OUR OTHER LABELS. THE BLUE LABEL ONLY HAS A DESIGN ASPECT I LIKE (PRIMER ON SIDE). The last four labels are our competitors.
```````````````````````````````````````````````````````````````````````````````````````````````````
We need this label to look professional, sharp, eye catching and modern.
OUR PRIMARY COLORS ARE BLACK AND WHITE. IF YOU INCOPORATE ANOTHER COLOR, SILVER OR GOLD MIGHT BE IDEAL BUT PLEASE DON'T DRIFT TOO FAR.
The attached documents:
1st - Our Logo
2nd - Our chalk paint label (reference). We do not need a chalk paint label.
3rd. A random design example. I like the BASE on the side running vertically. I think it's a cool design concept.
````````````````````````````````````````````````````````````````````````````````````````````````````
We are going to be using a normal paint can with a metal bail/handle so please use that with you design work
``````````````````````````````````````````````````````````````````````````````````````````````````
Order, in my head:
2743
Coatings
^^ I want this to stand out as well but I don't want it to be the first thing your eye is drawn to. Probably 2nd
Interior/Exterior
Multi - Surface Primer
^^ Want this to stick out and draw your eye so the customer knows what it is immediately
Exceptional Adhesion, Performance, Durability,
Use on Wood, Drywall, Plaster, Stucco, Masonry, Brick, Paneling, Painted Metal, & Properly Prepared Glossy Surfaces & More
35* Lowe Temperature Application (can be on side or small)
100% Acrylic
Low Odor - Low VOC - Soap & Water Clean Up
1 US Gallon - 3.785 L
Feel free to get creative with it!

```html
<!DOCTYPE html>
<html lang="en">
<head>
<meta charset="utf-8">
<title>2743 Coatings – Base Primer Label</title>
<link href="https://fonts.googleapis.com/css2?family=Roboto:wght@400;500;700&display=swap" rel="stylesheet">
<style>
  :root {
    --backdrop: #aca99f;
    --ink: #111111;
    --label-black: #050505;
    --white: #ffffff;
    --line-silver: #c9c2b7;
    --silver-dark: #7a7166;
    --silver-mid: #b9b4ac;
    --silver-light: #eeece8;
    --rule: #2a2a2a;
  }
  * { box-sizing: border-box; margin: 0; padding: 0; }
  html, body { width: 1110px; height: 1200px; overflow: hidden; }
  body {
    background: radial-gradient(ellipse at 50% 45%, #c4c1ba 0%, var(--backdrop) 70%);
    position: relative;
    font-family: "Roboto", Arial, sans-serif;
    color: var(--ink);
  }

  .company-name {
    position: absolute;
    font-family: "Roboto", Arial, sans-serif;
    font-weight: 500;
    line-height: 1;
    white-space: nowrap;
  }
  .company-name.page-corner { left: 54px; top: 60px; font-size: 44px; color: var(--ink); }

  .label {
    position: absolute;
    left: 50px; top: 420px;
    width: 1010px; height: 484px;
    background: var(--label-black);
    overflow: hidden;
  }

  .line-name {
    position: absolute; left: 190px; top: 60px;
    width: 110px; height: 400px;
  }

  .company-name.on-label {
    left: 314px; top: 120px; width: 382px;
    text-align: center; font-size: 46px; color: var(--white);
  }

  .spec-panel {
    position: absolute;
    left: 314px; top: 211px;
    width: 382px; height: 273px;
    background: linear-gradient(90deg, var(--silver-dark) 0%, #a59d92 14%, var(--silver-light) 38%, #d6d3ce 55%, var(--silver-mid) 75%, var(--silver-light) 100%);
    text-align: center;
  }
  .product-type {
    position: absolute; left: 0; right: 0;
    font-weight: 700; line-height: 1; color: var(--ink);
  }
  .product-type.line-a { top: 20px; font-size: 27px; }
  .product-type.line-b { top: 54px; font-size: 27px; }
  .product-name { position: absolute; left: 0; right: 0; top: 87px; font-size: 40px; font-weight: 700; line-height: 1; }

  .resin-pill {
    position: absolute; left: 105px; top: 130px;
    width: 172px; height: 27px;
    background: var(--ink); color: var(--white);
    border-radius: 6px 6px 0 0;
    font-size: 17px; font-weight: 700; line-height: 27px;
  }

  .spec-table {
    position: absolute; left: 26px; top: 157px;
    width: 330px; height: 56px;
    border: 1px solid var(--rule);
    display: flex;
  }
  .volume-cell {
    width: 62px; border-right: 1px solid var(--rule);
    font-size: 11.5px; font-weight: 500; line-height: 1.1;
    padding-top: 4px; position: relative;
  }
  .volume-cell .metric {
    position: absolute; left: 2px; right: 2px; bottom: 2px;
    background: var(--ink); color: var(--white);
    font-size: 11px; font-weight: 700; line-height: 15px;
  }
  .claims-cell { flex: 1; display: flex; flex-direction: column; }
  .claims-cell .benefits {
    font-size: 9.6px; font-weight: 500; line-height: 20px;
    border-bottom: 1px solid var(--rule);
    white-space: nowrap;
  }
  .claims-cell .surfaces { font-size: 7.2px; font-weight: 500; line-height: 1.45; padding-top: 5px; white-space: nowrap; }

  .footer-line {
    position: absolute; left: 26px; top: 218px; width: 330px;
    display: flex; align-items: center; justify-content: center; gap: 6px;
    white-space: nowrap;
  }
  .footer-line .temp { font-size: 6.2px; display: flex; align-items: center; gap: 3px; color: #333; }
  .footer-line .divider { width: 1px; height: 14px; background: var(--rule); }
  .footer-line .care { font-size: 9.4px; font-weight: 500; }
</style>
</head>
<body>

  <div class="company-name page-corner">2743 Coatings</div>

  <section class="label">
    <svg class="line-name" viewBox="0 0 110 400" aria-label="Base">
      <text transform="translate(100,395) rotate(-90)" font-family="Roboto, Arial, sans-serif" font-weight="400" font-size="130" fill="#c9c2b7" textLength="330" lengthAdjust="spacingAndGlyphs">Base</text>
    </svg>

    <div class="company-name on-label">2743 Coatings</div>

    <div class="spec-panel">
      <div class="product-type line-a">INTERIOR/EXTERIOR</div>
      <div class="product-type line-b">MULTI - SURFACE</div>
      <div class="product-name">PRIMER</div>
      <div class="resin-pill">100% Acrylic</div>

      <div class="spec-table">
        <div class="volume-cell">1 US<br>Gallon<span class="metric">3.785 L</span></div>
        <div class="claims-cell">
          <div class="benefits">EXCEPTIONAL ADHESION | PERFORMANCE | DURABILITY</div>
          <div class="surfaces">Use on Wood | Drywall | Plaster | Stucco | Masonry | Brick<br>Paneling | Painted Metal | &amp; Properly Prepared Glossy Surfaces &amp; More</div>
        </div>
      </div>

      <div class="footer-line">
        <span class="temp">
          <svg width="5" height="9" viewBox="0 0 5 9" aria-hidden="true"><rect x="1.5" y="0" width="2" height="6" rx="1" fill="#333"/><circle cx="2.5" cy="7" r="2" fill="#333"/></svg>
          35+ Low Temperature Application
        </span>
        <span class="divider"></span>
        <span class="care">Low Odor - Low VOC - Soap &amp; Water Clean Up</span>
      </div>
    </div>
  </section>

</body>
</html>
```